Occupational Therapy Clinic Advertisement

Create an advertisement for a magazine. Below I have attached my original ad (Ad 2020.pdf) . I want the ad changed and it should be eye catching. I would like a eye catching graphics added in the ad. It should be a graphic image that applies to education. I am attaching a sample graphic image of that I liked from someone elses ad- it should not be the same- it just is there to show what I like. Please use the same words from my original ad.Dimensions: 3.75in x 10.3 in

Target Market(s)

Parents of School aged children

Requirements
Must have
• Must have eye catching Graphic. Colors should be eye catching for a typed magazine.

```html
<!DOCTYPE html>
<html lang="en">
<head>
<meta charset="utf-8">
<title>Bright Step OT Services</title>
<link rel="stylesheet" href="https://fonts.googleapis.com/css2?family=Arimo:wght@400;700&family=Carlito:wght@400;700&family=Libre+Baskerville:wght@700&family=Tinos&display=swap">
<style>
:root{
  --navy:#000060;
  --ring:#3f5186;
  --ring-light:#f7f4f2;
  --green:#5aa94a;
  --white:#ffffff;
  --yellow:#ffff00;
  --red:#e0141e;
}
*{margin:0;padding:0;box-sizing:border-box}
html,body{width:1200px;height:3291px;overflow:hidden;background:var(--white)}
.ad{position:relative;width:1200px;height:3291px;border:2px solid #222;overflow:hidden;color:var(--navy);font-family:"Carlito",sans-serif}
.abs{position:absolute}
.center{text-align:center;left:0;right:0}
.brand{left:40px;top:40px;font-family:"Arimo",sans-serif;font-weight:700;font-size:84px;letter-spacing:1px}
.brand-sub{left:190px;top:164px;font-family:"Tinos",serif;font-size:56px}
.phone-top{right:44px;top:88px;font-family:"Arimo",sans-serif;font-size:54px}
.hero{top:0;left:0;width:1200px;height:1230px}
.question{font-size:82px;line-height:100px}
.divider{left:88px;width:994px;height:8px;background:var(--navy);border-radius:50%}
.band{top:1230px;left:0;width:1200px;height:556px;background:var(--navy)}
.promise{left:0;width:664px;top:1318px;text-align:center;font-family:"Libre Baskerville",serif;font-weight:700;color:var(--white);font-size:69px;line-height:92px}
.promise .struck{color:var(--yellow);position:relative;display:inline-block}
.promise .struck::after{content:"";position:absolute;left:-4px;right:10px;top:50%;height:5px;background:var(--red);transform:rotate(-28deg)}
.target-art{left:652px;top:1329px;width:548px;height:457px;border-top-left-radius:60% 70%;background:radial-gradient(ellipse at 72% 58%,var(--ring-light) 0%,#b9bfd2 30%,var(--ring) 62%,var(--navy) 100%)}
.pill{background:var(--navy);color:var(--white);border-radius:12px;font-weight:700;text-align:center}
.body-text{font-size:74px;line-height:92px;text-align:center}
.green-bar{left:0;width:1200px;background:var(--green);color:var(--white);font-weight:700;text-align:center}
.info{font-family:"Arimo",sans-serif;text-align:center;left:0;right:0}
</style>
</head>
<body>
<div class="ad">
  <svg class="abs hero" width="1200" height="1230" viewBox="0 0 1200 1230" aria-hidden="true">
    <defs>
      <linearGradient id="sky" x1="0" y1="0" x2="0" y2="1">
        <stop offset="0" stop-color="#9dbcd8"/>
        <stop offset="1" stop-color="#ffffff"/>
      </linearGradient>
    </defs>
    <path d="M0 240 H665 L703 172 H1200 V1160 H0 Z" fill="url(#sky)"/>
  </svg>

  <div class="abs brand">Bright Step</div>
  <div class="abs brand-sub">OT Services</div>
  <div class="abs phone-top">(555) 014-2286</div>

  <div class="abs center question" style="top:363px">Does your child struggle<br>with Reading/Kriah?</div>
  <div class="abs divider" style="top:606px"></div>
  <div class="abs center question" style="top:662px">Knows the information<br>but fails the test?</div>
  <div class="abs divider" style="top:908px"></div>
  <div class="abs center question" style="top:958px">Has difficulty remembering<br>names and dates?</div>

  <div class="abs band"></div>
  <div class="abs promise">Yes Your Child<br><span class="struck">can</span><br>Will Succeed<br>in School!</div>
  <div class="abs target-art" role="img" aria-label="Illustration: a dart striking the bullseye of a blue and white target"></div>

  <div class="abs pill" style="left:98px;top:1894px;width:435px;height:87px;font-size:74px;line-height:87px">We Evaluate:</div>
  <div class="abs body-text" style="left:20px;width:600px;top:1976px">Using standardized<br>Evaluations</div>

  <div class="abs pill" style="left:98px;top:2252px;width:435px;height:87px;font-size:74px;line-height:87px">We Treat:</div>
  <div class="abs body-text" style="left:10px;width:600px;top:2339px">Using Researched<br>based techniques</div>

  <div class="abs body-text" style="left:680px;width:500px;top:1912px;font-size:78px;line-height:77px">We Treat the<br>underlying<br>processing<br>deficits</div>

  <div class="abs pill" style="left:780px;top:2297px;width:274px;height:99px;font-size:86px;line-height:99px">Ages</div>
  <div class="abs body-text" style="left:717px;width:400px;top:2408px;font-size:88px">6-18</div>

  <div class="abs green-bar" style="top:2556px;height:113px;font-size:76px;line-height:113px">Board of Ed OT RSA's accepted</div>

  <div class="abs info" style="top:2712px;font-size:58px">Located in Borough Park</div>
  <div class="abs info" style="top:2830px;font-size:48px">Evaluations done in Borough Park &amp; Staten Island</div>
  <div class="abs info" style="top:2934px;font-size:48px">For more information or to be added to our email list,</div>
  <div class="abs info" style="top:3038px;font-size:48px">please email: brightstepot@example.com</div>

  <div class="abs green-bar" style="top:3134px;height:157px;font-size:50px;line-height:58px;padding-top:18px">Dina Marcovitz OTR/L<br>(555)014-2286</div>
</div>
</body>
</html>
```